Membership Based Medical Practice Website

We need a functioning website for a new Membership based medical practice. There will be an enrollment fee and a monthly fee. We would like to see designs that are modern, simple. Should use neutral light colors. Examples of sites we like are www.tallowbrookclinic.com and https://medicnearquill.com/ We also have a link that when "Join Now" is clicked it will go to the signup website.

Target Market(s)

Gay Men, local population, Age group 20 to 60's.

Industry/Entity Type

Medical

Coding

Coded - Design and coding required

Number of Pages Required

5+ page

Font styles to use
Sans Serif

Colors
ffffff
cee9f5
ecf7fb
cfeae6
edf8f6
aaaaaa
e9e9e9
dbdbdb
fff3d1

Requirements
Must have
• Logo and header on every page. Clean, simple design, clear content, mobile compatible.
• Must use Wordpress
Nice to have
• Ideas should come from tallowbrookclinic.com
• Easy to read
Should not have
• Generic patient pictures, bold colors.
• Should not copy from above websites.

```html
<!DOCTYPE html>
<html lang="en">
<head>
<meta charset="utf-8">
<title>Harborline Infectious Disease Specialists</title>
<link href="https://fonts.googleapis.com/css2?family=Montserrat:wght@400;500;600;700&family=Open+Sans:wght@400;600&display=swap" rel="stylesheet">
<style>
:root{
  --white:#ffffff;
  --footer:#c2e3f2;
  --grey:#aaaaaa;
  --line:#e9e9e9;
  --rule:#dbdbdb;
  --cream:#fff3d1;
  --gold:#c9a45c;
  --ink:#2b2b2b;
  --body:#555555;
  --soft:#f2f2f2;
  --icon:#8a8a8a;
}
*{margin:0;padding:0;box-sizing:border-box}
html,body{width:1200px;height:3991px;overflow:hidden}
body{position:relative;background:var(--white);font-family:"Open Sans",Arial,sans-serif;color:var(--body)}
.abs{position:absolute}
h2,h3,.nav,.btn,.caps{font-family:"Montserrat",Arial,sans-serif}

/* header + hero */
.hero{left:0;top:0;width:1200px;height:652px;background:radial-gradient(ellipse 520px 300px at 560px 240px,#f7dc9a 0%,rgba(247,220,154,0) 100%),linear-gradient(180deg,#c99a52 0%,#d9a54d 30%,#b57a32 55%,#7b5526 78%,#4d3a1e 100%);overflow:hidden}
.hero-curve{left:0;top:540px}
.brand{left:58px;top:22px;width:230px;text-align:center;color:var(--white)}
.brand-mark{width:62px;height:62px;border:2px solid var(--gold);border-radius:50%;margin:0 auto 10px}
.brand-name{font-family:"Montserrat",Arial,sans-serif;font-size:17px;letter-spacing:10px;font-weight:500}
.brand-sub{font-family:"Montserrat",Arial,sans-serif;font-size:11px;letter-spacing:1px;margin-top:2px}
.nav{right:40px;top:32px;display:flex;gap:30px;align-items:center;font-size:13px;font-weight:500;color:var(--white)}
.nav .current{border-bottom:2px solid var(--white);padding-bottom:3px}
.nav .join{background:var(--cream);color:var(--ink);padding:8px 14px}
.hero-title{left:788px;top:448px;width:380px;color:var(--white);font-family:"Montserrat",Arial,sans-serif;font-weight:700;font-size:31px;line-height:36px}
.dots{left:548px;top:596px;display:flex;gap:12px;align-items:center}
.dots span{width:7px;height:7px;border-radius:50%;background:var(--white)}
.dots .on{width:11px;height:11px;background:none;border:2px solid var(--white)}

/* areas */
.areas-title{left:0;top:735px;width:1200px;text-align:center;font-size:20px;font-weight:700;line-height:32px;color:var(--ink);letter-spacing:.5px}
.areas-tag{left:427px;top:830px;width:346px;height:40px;background:var(--white);box-shadow:0 0 18px rgba(0,0,0,.08);text-align:center;line-height:40px;font-size:16px;color:#333}
.areas-band{left:0;top:880px;width:1200px;height:387px;background:var(--soft)}
.card{top:926px;width:192px;height:186px;background:var(--white);box-shadow:0 2px 10px rgba(0,0,0,.06);text-align:center}
.card svg{display:block;margin:24px auto 0}
.card p{font-family:"Montserrat",Arial,sans-serif;font-size:11px;font-weight:700;color:#333;margin-top:22px;line-height:15px;padding:0 8px}
.arrow{top:1012px}
.btn{background:var(--cream);color:var(--ink);font-size:12px;font-weight:700;text-align:center;border:2px solid #f0dfae;letter-spacing:.5px}
.btn-areas{left:516px;top:1166px;width:168px;height:44px;line-height:40px}

/* road band */
.road{left:0;top:1267px;width:1200px;height:447px;background:radial-gradient(ellipse 300px 90px at 600px 300px,#eef0f0 0%,rgba(238,240,240,0) 100%),linear-gradient(180deg,#b9bfc4 0%,#d4d8da 38%,#a5ae9a 56%,#6a7a55 72%,#465338 100%)}
.road-line{left:0;top:1267px}
.road-frame-top{left:271px;top:1317px;width:656px;height:3px;background:var(--white)}
.road-frame-left{left:271px;top:1317px;width:3px;height:96px;background:var(--white)}
.road-frame-right{left:924px;top:1317px;width:3px;height:253px;background:var(--white)}
.road-title{left:271px;top:1388px;width:656px;text-align:center;font-size:26px;font-weight:700;color:#222}
.road-sub{left:271px;top:1432px;width:656px;text-align:center;font-size:19px;font-weight:500;color:#333;letter-spacing:.5px}

/* why */
.why-title{left:0;top:1775px;width:1200px;text-align:center;font-size:26px;font-weight:700;color:var(--ink);letter-spacing:1px}
.why-rule{left:585px;top:1826px;width:30px;height:2px;background:#999}
.feature{width:330px}
.feature .ico{position:absolute;top:0;width:54px;height:54px;border-radius:50%;border:1px solid var(--rule);background:var(--white);box-shadow:0 2px 6px rgba(0,0,0,.08);display:flex;align-items:center;justify-content:center}
.feature h3{font-size:12px;font-weight:700;color:var(--ink);letter-spacing:.3px}
.feature p{font-size:12.5px;line-height:16px;margin-top:6px;color:#555}
.feature .rule{position:absolute;height:1px;background:var(--line);width:250px;top:88px}
.left .ico{left:0}.left .txt{position:absolute;left:74px;top:0;width:240px}.left .rule{left:74px}
.right .ico{right:0}.right .txt{position:absolute;left:0;top:0;width:250px}.right .rule{left:0}
.why-mark{left:424px;top:1910px;width:330px;height:290px}

/* pricing */
.pricing{left:0;top:2352px;width:1200px;height:602px;background:radial-gradient(ellipse 260px 180px at 560px 420px,#ffd79a 0%,rgba(255,215,154,0) 100%),linear-gradient(180deg,#efe8ef 0%,#f0e2e2 45%,#e8b98a 68%,#c48650 82%,#7d5a46 100%)}
.pricing-title{left:0;top:2400px;width:1200px;text-align:center;font-size:29px;line-height:38px;font-weight:700;color:var(--ink);letter-spacing:.5px}
.price-box{top:2512px;height:136px;background:var(--white);padding:26px 0 0 38px;color:#222;box-shadow:0 4px 14px rgba(0,0,0,.06)}
.price-box .label{font-family:"Montserrat",Arial,sans-serif;font-size:24px;font-weight:500;letter-spacing:.5px}
.price-box .amount{font-family:"Montserrat",Arial,sans-serif;font-size:35px;font-weight:700;margin-top:4px}
.price-box .amount small{font-size:16px;font-weight:700;margin-left:10px}

/* about */
.about-title{left:152px;top:3066px;font-size:27px;font-weight:700;color:var(--ink);letter-spacing:.5px}
.about-rule{left:152px;top:3106px;width:28px;height:2px;background:#999}
.checks{left:152px;top:3150px;width:330px;list-style:none}
.checks li{position:relative;padding-left:28px;font-size:14px;line-height:18px;color:#444;margin-bottom:24px}
.checks li svg{position:absolute;left:0;top:2px}
.btn-about{left:154px;top:3441px;width:208px;height:42px;line-height:38px}
.about-frame{left:508px;top:3039px;width:524px;height:481px;border:2px solid var(--cream)}
.about-photo{left:548px;top:3028px;width:500px;height:463px;background:radial-gradient(ellipse 120px 170px at 260px 270px,#f4f2ee 0%,#e2ddd6 55%,rgba(226,221,214,0) 100%),radial-gradient(ellipse 260px 300px at 240px 280px,#8e2a33 0%,#6d1f2a 55%,rgba(109,31,42,0) 100%),linear-gradient(160deg,#5a7ea6 0%,#3c5e85 50%,#2b425f 100%)}

/* footer */
.footer{left:0;top:3606px;width:1200px;height:385px;background:var(--footer)}
.foot-brand{left:146px;top:3690px;width:230px;height:230px;border:3px solid var(--white);border-radius:50%;display:flex;align-items:center;justify-content:center;text-align:center;font-family:"Montserrat",Arial,sans-serif;font-weight:600;color:var(--white);font-size:20px;letter-spacing:3px}
.col h4{font-family:"Montserrat",Arial,sans-serif;font-size:11px;font-weight:700;color:#222;letter-spacing:.3px;margin-bottom:18px}
.col li{list-style:none;font-size:11px;line-height:16px;color:#333;font-family:"Montserrat",Arial,sans-serif}
.contact li{position:relative;padding-left:22px;margin-bottom:18px}
.contact svg{position:absolute;left:0;top:1px}
.social li{display:flex;align-items:center;gap:10px;margin-bottom:14px}
.social .dot{width:24px;height:24px;border-radius:50%;background:#2d5b9a}
.foot-rule{left:468px;top:3877px;width:583px;height:1px;background:#9fc9dc}
.copyright{left:468px;top:3916px;width:583px;text-align:center;font-size:11px;color:#333;font-family:"Montserrat",Arial,sans-serif}
</style>
</head>
<body>

<section class="hero abs" role="img" aria-label="Photo: a family running through a sunlit golden meadow at sunset"></section>
<svg class="hero-curve abs" width="1200" height="112" viewBox="0 0 1200 112" aria-hidden="true"><path d="M0 72 Q600 140 1200 8 L1200 112 L0 112 Z" fill="#ffffff"/></svg>

<header>
  <div class="brand abs">
    <div class="brand-mark"></div>
    <div class="brand-name">HARBORLINE</div>
    <div class="brand-sub">INFECTIOUS DISEASE SPECIALISTS</div>
  </div>
  <nav class="nav abs">
    <span class="current">HOME</span><span>SPECIALTIES</span><span>PRICING</span><span>ABOUT US</span><span>FAQ</span><span>BLOG</span><span class="join">JOIN US</span>
  </nav>
</header>
<h1 class="hero-title abs">SPECIALTY MEDICINE WITH COMMITMENT, COMPASSION AND CARE</h1>
<div class="dots abs"><span></span><span></span><span class="on"></span><span></span><span></span></div>

<section>
  <div class="areas-band abs"></div>
  <h2 class="areas-title abs">WE OFFER COMPREHENSIVE TREATMENT<br>OF A WIDE VARIETY OF INFECTIOUS DISEASES.</h2>
  <div class="areas-tag abs">Out expertise is in the following area.</div>
  <svg class="arrow abs" style="left:50px" width="12" height="20" viewBox="0 0 12 20"><path d="M10 2 L2 10 L10 18" stroke="#aaa" stroke-width="2" fill="none"/></svg>
  <svg class="arrow abs" style="left:1142px" width="12" height="20" viewBox="0 0 12 20"><path d="M2 2 L10 10 L2 18" stroke="#aaa" stroke-width="2" fill="none"/></svg>

  <div class="card abs" style="left:106px">
    <svg width="80" height="70" viewBox="0 0 80 70" aria-hidden="true"><g fill="none" stroke="#8a8a8a" stroke-width="3"><rect x="4" y="10" width="34" height="18" rx="9" transform="rotate(25 21 19)"/><rect x="42" y="10" width="34" height="18" rx="9" transform="rotate(-25 59 19)"/></g><g fill="#8a8a8a"><circle cx="40" cy="44" r="3"/><circle cx="35" cy="54" r="2.5"/><circle cx="44" cy="62" r="2"/></g></svg>
    <p>HIV/PREP</p>
  </div>
  <div class="card abs" style="left:309px">
    <svg width="80" height="70" viewBox="0 0 80 70" aria-hidden="true"><g fill="none" stroke="#8a8a8a" stroke-width="2.5"><circle cx="40" cy="35" r="16"/><path d="M40 19V7M40 51V63M24 35H12M56 35H68M29 24L21 16M51 46L59 54M51 24L59 16M29 46L21 54"/></g><g fill="#8a8a8a"><circle cx="40" cy="6" r="3.5"/><circle cx="40" cy="64" r="3.5"/><circle cx="11" cy="35" r="3.5"/><circle cx="69" cy="35" r="3.5"/><circle cx="20" cy="15" r="3"/><circle cx="60" cy="55" r="3"/><circle cx="60" cy="15" r="3"/><circle cx="20" cy="55" r="3"/><circle cx="36" cy="32" r="2.5"/><circle cx="45" cy="39" r="2.5"/></g></svg>
    <p>CHRONIC<br>HEPATITIS</p>
  </div>
  <div class="card abs" style="left:511px">
    <svg width="80" height="70" viewBox="0 0 80 70" aria-hidden="true"><path d="M14 24 C26 14 52 12 66 18 C72 22 66 34 56 42 C48 50 40 60 36 62 C30 50 20 40 14 24 Z" fill="#8a8a8a"/></svg>
    <p>CHRONIC<br>HEPATITIS</p>
  </div>
  <div class="card abs" style="left:713px">
    <svg width="80" height="70" viewBox="0 0 80 70" aria-hidden="true"><g fill="none" stroke="#8a8a8a" stroke-width="2.5"><path d="M33 4 V26 C33 30 30 31 30 34 H50 C50 31 47 30 47 26 V4"/><circle cx="40" cy="38" r="5"/><path d="M30 42 C30 45 33 46 33 50 V68 M47 68 V50 C47 46 50 45 50 42 Z"/></g></svg>
    <p>BONE AND<br>JOINT INFECTIONS</p>
  </div>
  <div class="card abs" style="left:913px">
    <svg width="80" height="70" viewBox="0 0 80 70" aria-hidden="true"><g fill="#8a8a8a"><circle cx="30" cy="28" r="11"/><circle cx="50" cy="22" r="9"/><circle cx="48" cy="44" r="12"/><circle cx="28" cy="50" r="8"/></g><g fill="#ffffff"><circle cx="27" cy="26" r="2"/><circle cx="51" cy="21" r="2"/><circle cx="46" cy="42" r="2.5"/><circle cx="52" cy="48" r="1.8"/></g></svg>
    <p>INFECTIONS ASSOCIATED<br>WITH MEDICAL DEVICES</p>
  </div>
  <div class="btn btn-areas abs">VIEW ALL AREAS</div>
</section>

<section>
  <div class="road abs" role="img" aria-label="Photo: an empty road running through misty green hills"></div>
  <div class="road-frame-top abs"></div><div class="road-frame-left abs"></div><div class="road-frame-right abs"></div>
  <h2 class="road-title abs">LESS WAIT, MORE PERSONAL.</h2>
  <p class="road-sub abs caps">WE ARE NOT YOUR TRADITIONAL DOCTOR'S OFFICE.</p>
</section>

<section>
  <h2 class="why-title abs">WHY CHOOSE US</h2>
  <div class="why-rule abs"></div>

  <div class="feature left abs" style="left:128px;top:1895px"><span class="ico"><svg width="24" height="24" viewBox="0 0 24 24" aria-hidden="true"><g fill="none" stroke="#8a8a8a" stroke-width="2"><circle cx="12" cy="8" r="5"/><path d="M3 20 C6 15 9 16 12 17 L18 15 C20 15 21 17 19 18 L12 21 L3 21"/></g></svg></span><div class="txt"><h3>STRAIGHTFORWARD PRICING</h3><p>We charge all our patients the same low rate - no surprises.</p></div><span class="rule"></span></div>
  <div class="feature left abs" style="left:128px;top:1990px"><span class="ico"><svg width="24" height="24" viewBox="0 0 24 24" aria-hidden="true"><g fill="none" stroke="#8a8a8a" stroke-width="2"><rect x="3" y="5" width="18" height="16" rx="1"/><path d="M3 10H21M8 3V7M16 3V7M7 14H9M11 14H13M15 14H17M7 17H9M11 17H13"/></g></svg></span><div class="txt"><h3>AVAILABLE WHEN YOU ARE</h3><p>New patient appointments are available within 1 week.</p></div><span class="rule"></span></div>
  <div class="feature left abs" style="left:128px;top:2088px"><span class="ico"><svg width="24" height="24" viewBox="0 0 24 24" aria-hidden="true"><g fill="none" stroke="#8a8a8a" stroke-width="2"><rect x="3" y="4" width="15" height="17" rx="1"/><path d="M9 15 L19 5 L21 7 L11 17 L8 18 Z"/></g></svg></span><div class="txt"><h3>HASSLE-FREE BOOKING</h3><p>Schedule your appointment online at your convenience - no need to call during business hours.</p></div><span class="rule"></span></div>
  <div class="feature left abs" style="left:128px;top:2202px"><span class="ico"><svg width="24" height="24" viewBox="0 0 24 24" aria-hidden="true"><path d="M3 4H21V16H10L5 20V16H3Z" fill="#8a8a8a"/><g fill="#fff"><circle cx="8" cy="10" r="1.3"/><circle cx="12" cy="10" r="1.3"/><circle cx="16" cy="10" r="1.3"/></g></svg></span><div class="txt"><h3>DEVOTED CARE</h3><p>We schedule enough time at each visit to make sure all of your questions are answered.</p></div></div>

  <div class="why-mark abs"><svg width="330" height="290" viewBox="0 0 330 290" aria-hidden="true"><circle cx="165" cy="145" r="120" fill="none" stroke="#c9a45c" stroke-width="3"/><text x="165" y="153" text-anchor="middle" font-family="Montserrat, Arial, sans-serif" font-size="24" font-weight="600" fill="#c9a45c" letter-spacing="3">HARBORLINE</text></svg></div>

  <div class="feature right abs" style="left:782px;top:1895px"><span class="ico"><svg width="24" height="24" viewBox="0 0 24 24" aria-hidden="true"><path d="M4 4H20V16H11L6 20V16H4Z" fill="#8a8a8a"/><rect x="8" y="8" width="8" height="4" fill="#fff"/></svg></span><div class="txt"><h3>WITHIN YOUR REACH</h3><p>Follow-up appointments may be done by video chat for your convenience.</p></div><span class="rule"></span></div>
  <div class="feature right abs" style="left:782px;top:1990px"><span class="ico"><svg width="24" height="24" viewBox="0 0 24 24" aria-hidden="true"><g fill="#8a8a8a"><ellipse cx="12" cy="13" rx="8" ry="6"/><rect x="7" y="17" width="3" height="4"/><rect x="14" y="17" width="3" height="4"/><rect x="19" y="11" width="3" height="3"/><circle cx="12" cy="5" r="2"/></g></svg></span><div class="txt"><h3>SAVE ON LAB COSTS</h3><p>If paying upfront for labs, we offer discounted pricing of up to 90% off standard rates.</p></div><span class="rule"></span></div>
  <div class="feature right abs" style="left:782px;top:2088px"><span class="ico"><svg width="24" height="24" viewBox="0 0 24 24" aria-hidden="true"><g fill="none" stroke="#8a8a8a" stroke-width="2"><rect x="4" y="7" width="9" height="14" rx="1"/><path d="M5 3H12V7H5Z"/><rect x="15" y="12" width="6" height="9" rx="3"/></g></svg></span><div class="txt"><h3>SAVE ON MEDICATIONS</h3><p>We offer deeply discounted wholesale price medications for our members at pharmacy on site.</p></div><span class="rule"></span></div>
  <div class="feature right abs" style="left:782px;top:2202px"><span class="ico"><svg width="24" height="24" viewBox="0 0 24 24" aria-hidden="true"><g fill="#8a8a8a"><circle cx="12" cy="7" r="5"/><path d="M3 22 C3 15 7 13 12 13 C17 13 21 15 21 22 Z"/></g></svg></span><div class="txt"><h3>NO MIDDLE MAN</h3><p>We don't bill any insurance plans so decisions about your healthcare will be made by you and Dr. Ravel.</p></div></div>
</section>

<section>
  <div class="pricing abs" role="img" aria-label="Photo: four friends embracing, seen from behind at sunset"></div>
  <h2 class="pricing-title abs">OUR PRICING IS SIMPLE,<br>TRANSPARENT AND AFFORDABLE.</h2>
  <div class="price-box abs" style="left:266px;width:319px"><div class="label">MEMBERSHIP PLAN</div><div class="amount">$ 80/MO</div></div>
  <div class="price-box abs" style="left:604px;width:322px"><div class="label">PLUS A ONE-TIME</div><div class="amount">$ 99<small>Enrollment FEE</small></div></div>
</section>

<section>
  <h2 class="about-title abs">ABOUT US</h2>
  <div class="about-rule abs"></div>
  <ul class="checks abs">
    <li><svg width="14" height="12" viewBox="0 0 14 12"><path d="M1 6 L5 10 L13 1" stroke="#8cc9bd" stroke-width="2" fill="none"/></svg>Includes all appointments, no co-pay</li>
    <li><svg width="14" height="12" viewBox="0 0 14 12"><path d="M1 6 L5 10 L13 1" stroke="#8cc9bd" stroke-width="2" fill="none"/></svg>Relaxed, unrushed visits</li>
    <li><svg width="14" height="12" viewBox="0 0 14 12"><path d="M1 6 L5 10 L13 1" stroke="#8cc9bd" stroke-width="2" fill="none"/></svg>Direct communication with your doctor via phone, email, video chat 24/7</li>
    <li><svg width="14" height="12" viewBox="0 0 14 12"><path d="M1 6 L5 10 L13 1" stroke="#8cc9bd" stroke-width="2" fill="none"/></svg>Convenient online scheduling (no need to call during business hours)</li>
    <li><svg width="14" height="12" viewBox="0 0 14 12"><path d="M1 6 L5 10 L13 1" stroke="#8cc9bd" stroke-width="2" fill="none"/></svg>Wholesale price for labs and medications</li>
  </ul>
  <div class="btn btn-about abs">LEARN MORE ABOUT US</div>
  <div class="about-frame abs"></div>
  <div class="about-photo abs" role="img" aria-label="Photo: a hand holding a white enamel camping mug heaped with snow"></div>
</section>

<footer>
  <div class="footer abs"></div>
  <div class="foot-brand abs">HARBORLINE</div>
  <div class="col contact abs" style="left:468px;top:3676px;width:220px">
    <h4>CONTACT US</h4>
    <ul>
      <li><svg width="10" height="14" viewBox="0 0 10 14"><path d="M5 0 C2 0 0 2 0 5 C0 9 5 14 5 14 C5 14 10 9 10 5 C10 2 8 0 5 0 Z" fill="#333"/><circle cx="5" cy="5" r="2" fill="#c2e3f2"/></svg>718 Millrace Avenue<br>Dunmore, IL 60499</li>
      <li><svg width="12" height="12" viewBox="0 0 12 12"><path d="M2 0 L5 3 L3.5 5 C4.5 7 5 7.5 7 8.5 L9 7 L12 10 L10 12 C5 12 0 7 0 2 Z" fill="#333"/></svg>555.014.2290</li>
      <li><svg width="13" height="10" viewBox="0 0 13 10"><rect width="13" height="10" fill="#333"/><path d="M0 0 L6.5 5 L13 0" stroke="#c2e3f2" fill="none"/></svg>info@harborlineid.com</li>
    </ul>
  </div>
  <div class="col abs" style="left:729px;top:3676px">
    <h4>MENU</h4>
    <ul><li>HOME</li><li>SPECIALTIES</li><li>PRICING</li><li>ABOUT US</li><li>FAQ</li><li>BLOG</li><li>JOIN US</li></ul>
  </div>
  <div class="col social abs" style="left:937px;top:3676px">
    <h4>CONNECT WITH US</h4>
    <ul><li><span class="dot"></span>Friendpage</li><li><span class="dot" style="background:#3aa0e0"></span>Chirpline</li><li><span class="dot" style="background:#1d4f7a"></span>Workweb</li></ul>
  </div>
  <div class="foot-rule abs"></div>
  <p class="copyright abs">Copyrights @ 2019 All Rights Reserved</p>
</footer>

</body>
</html>
```